Wine Label Design

Organization name: Halvern Wine Company

My company is called Halvern Wine Company, I’m a wine importer and wholesaler who distributes wine domestically.

We are about to launch a line of three premium and one sparkling wine that we will wholesale to various retailers, wine stores, and restaurants for re-sale. The wines label will have “Dorian Halvern” I plan on having the labels the same and just changing the varietal as needed. My wine are made from premium grapes and will be marketed as a high end wine. My current label size is 3 1/2" wide by 5" in long and the labels can be on a solid background or transparent.

I would like the first label to be for my Cabernet Sauvignon, California, 2012, 750ML (for the size of the bottle) and ALC 13.8% BY VOL (for the alcohol content).

Colors: I am open to any and all designs that would alter my perception of what will be best!

Further:
Current label is boring and poorly done, so hopefully you designers can come up with something better

Industry/Entity Type

It Company

```html
<!DOCTYPE html>
<html lang="en">
<head>
<meta charset="utf-8">
<title>Halvern Wine – Cabernet Sauvignon Label</title>
<link rel="stylesheet" href="https://fonts.googleapis.com/css2?family=Arimo:wght@700&family=Tinos:wght@700&family=Playfair+Display:ital,wght@1,700&display=swap">
<style>
  :root {
    --leather-light: #3d3a37;
    --leather-dark: #1f1e1c;
    --gold-deep: #b8832a;
    --gold-bright: #f4d27c;
    --gold-text: #e9c46a;
    --mark-dark: #14161f;
    --panel-light: #8c8782;
    --panel-dark: #5e5a56;
    --ribbon-red: #86121d;
    --ribbon-text: #d9cfc4;
    --ink-dark: #2a1418;
    --white: #ffffff;
  }
  html, body {
    margin: 0;
    padding: 0;
    width: 1200px;
    height: 2500px;
    overflow: hidden;
    background: var(--leather-dark);
  }
  .label {
    position: relative;
    width: 1200px;
    height: 2500px;
    background: radial-gradient(ellipse at 50% 40%, var(--leather-light) 0%, var(--leather-dark) 85%);
    overflow: hidden;
  }
  .gold-band {
    position: absolute;
    left: 0;
    top: 250px;
    width: 1200px;
    height: 116px;
    background: linear-gradient(180deg, var(--gold-deep) 0%, var(--gold-bright) 50%, var(--gold-deep) 100%);
  }
  .brand-square {
    position: absolute;
    left: 505px;
    top: 213px;
    width: 190px;
    height: 190px;
    background: var(--mark-dark);
  }
  .brand-name {
    position: absolute;
    left: 0;
    width: 1200px;
    text-align: center;
    font-family: "Arimo", Arial, sans-serif;
    font-weight: 700;
    color: var(--white);
    margin: 0;
    line-height: 1;
    white-space: nowrap;
  }
  .brand-name--top { top: 566px; font-size: 224px; letter-spacing: -6px; }
  .brand-name--bottom { top: 752px; font-size: 340px; letter-spacing: -8px; }

  .quality-panel {
    position: absolute;
    left: 40px;
    top: 1232px;
    width: 1120px;
    height: 640px;
    background: linear-gradient(180deg, var(--panel-light) 0%, var(--panel-dark) 100%);
    box-shadow: inset 0 0 40px rgba(0,0,0,0.45);
  }
  .crown-art {
    position: absolute;
    left: 505px;
    top: 80px;
    width: 110px;
    height: 90px;
    background: var(--ribbon-red);
  }
  .quality-line {
    position: absolute;
    left: 0;
    width: 1120px;
    text-align: center;
    font-family: "Tinos", "Times New Roman", serif;
    font-weight: 700;
    margin: 0;
    line-height: 1;
  }
  .quality-line--small { top: 196px; font-size: 64px; color: var(--ink-dark); }
  .ribbon {
    position: absolute;
    left: 140px;
    top: 276px;
    width: 840px;
    height: 140px;
    background: var(--ribbon-red);
  }
  .quality-line--ribbon { top: 302px; font-size: 90px; color: var(--ribbon-text); letter-spacing: 2px; }
  .flourish-art {
    position: absolute;
    left: 300px;
    top: 440px;
    width: 520px;
    height: 90px;
    background: linear-gradient(180deg, rgba(30,20,20,0.55), rgba(30,20,20,0.25));
    border-radius: 45px;
  }
  .quality-line--owner { top: 560px; font-size: 48px; color: var(--ink-dark); letter-spacing: 4px; }

  .varietal {
    position: absolute;
    left: 0;
    width: 1200px;
    text-align: center;
    font-family: "Playfair Display", Georgia, serif;
    font-style: italic;
    font-weight: 700;
    font-size: 140px;
    color: var(--gold-text);
    margin: 0;
    line-height: 1;
  }
  .varietal--first { top: 2040px; }
  .varietal--second { top: 2170px; }
  .details {
    position: absolute;
    left: 0;
    width: 1200px;
    text-align: center;
    font-family: "Arimo", Arial, sans-serif;
    font-weight: 700;
    color: var(--white);
    margin: 0;
    line-height: 1;
    white-space: nowrap;
  }
  .details--origin { top: 2336px; font-size: 84px; }
  .details--alcohol { top: 2436px; font-size: 40px; letter-spacing: 3px; }
</style>
</head>
<body>
  <main class="label">
    <div class="gold-band"></div>
    <div class="brand-square"></div>
    <h1 class="brand-name brand-name--top">HALVERN</h1>
    <p class="brand-name brand-name--bottom">WINE</p>

    <section class="quality-panel">
      <div class="crown-art" role="img" aria-label="Small crown ornament"></div>
      <p class="quality-line quality-line--small">100 PERCENT</p>
      <div class="ribbon"></div>
      <p class="quality-line quality-line--ribbon">BEST QUALITY</p>
      <div class="flourish-art" role="img" aria-label="Decorative scroll flourish"></div>
      <p class="quality-line quality-line--owner">DORIAN HALVERN</p>
    </section>

    <p class="varietal varietal--first">Cabernet</p>
    <p class="varietal varietal--second">Sauvignon</p>
    <p class="details details--origin">CALIFORNIA,2012,750ML</p>
    <p class="details details--alcohol">ALC 13.8% BY VOL</p>
  </main>
</body>
</html>
```